Spices producer needs product label design.

I need a two label design of 90mm(H) x 60mm(H) for multiple line of spices and other product. First label for the front should have the logo, and second label should be the same as the first but without the logo. I would like the same dark reddish colour on my logo for the design if possible or similar. This label will be use for multiple products, so a clear in-between space is important to add information and change product name for printing . I would prefer a mixture of traditional and rustic style.
I have attached my logos and sample on how I would like the look.

Target Market(s)

25-60 women and men.

Industry/Entity Type

Retail

Requirements
Must have
• As stated above.
Nice to have
• Please see attached sample .
Should not have
• Multiple colours, animation design.

```html
<!DOCTYPE html>
<html lang="en">
<head>
<meta charset="utf-8">
<title>Spice label – front and back</title>
<link rel="stylesheet" href="https://fonts.googleapis.com/css2?family=Noto+Serif:ital,wght@0,800;1,600&family=Roboto+Condensed:wght@400&display=swap">
<style>
  :root {
    --label-red: #7a1416;
    --label-red-soft: #8a2a24;
    --cream: #f4e9d3;
    --ink: #111111;
    --page: #ffffff;
  }
  html, body {
    margin: 0;
    padding: 0;
    width: 1200px;
    height: 784px;
    overflow: hidden;
    background: var(--page);
  }
  .sheet {
    position: relative;
    width: 1200px;
    height: 784px;
  }
  .dimension {
    position: absolute;
    overflow: visible;
  }
  .dimension line {
    stroke: var(--ink);
    stroke-width: 1;
  }
  .dimension-text {
    position: absolute;
    font-family: "Roboto Condensed", sans-serif;
    font-size: 21px;
    color: var(--ink);
    white-space: nowrap;
    line-height: 1;
  }
  .dimension-text.vertical {
    transform: translate(-50%, -50%) rotate(-90deg);
  }
  .label {
    position: absolute;
    top: 128px;
    width: 359px;
    height: 539px;
    overflow: hidden;
  }
  .label-ornament {
    position: absolute;
    inset: 0;
    background: radial-gradient(circle at 30% 40%, var(--label-red-soft) 0%, var(--label-red) 70%);
  }
  .label-panel {
    position: absolute;
    left: 50px;
    top: 0;
    width: 260px;
    height: 449px;
    overflow: visible;
  }
  .panel-fill { fill: var(--cream); }
  .panel-rule { stroke: var(--label-red); stroke-width: 1.2; }
  .brand-name {
    position: absolute;
    left: 0;
    right: 0;
    top: 166px;
    margin: 0;
    text-align: center;
    font-family: "Noto Serif", serif;
    font-weight: 800;
    font-size: 46px;
    letter-spacing: 1px;
    line-height: 56px;
    color: var(--label-red);
  }
  .tagline-band {
    position: absolute;
    top: 245px;
    width: 203px;
    height: 29px;
    background: var(--label-red);
    display: flex;
    align-items: center;
    justify-content: center;
  }
  .tagline {
    margin: 0;
    font-family: "Noto Serif", serif;
    font-style: italic;
    font-weight: 600;
    font-size: 21px;
    color: var(--cream);
    line-height: 1;
  }
</style>
</head>
<body>
<main class="sheet">

  <!-- Front label dimensions -->
  <svg class="dimension" style="left:0;top:0" width="1200" height="784" aria-hidden="true">
    <line x1="196" y1="81" x2="196" y2="110"/>
    <line x1="555" y1="81" x2="555" y2="110"/>
    <line x1="196" y1="101" x2="555" y2="101"/>
    <line x1="142" y1="128" x2="171" y2="128"/>
    <line x1="142" y1="667" x2="171" y2="667"/>
    <line x1="156.5" y1="128" x2="156.5" y2="667"/>

    <line x1="686" y1="81" x2="686" y2="110"/>
    <line x1="1045" y1="81" x2="1045" y2="110"/>
    <line x1="686" y1="101" x2="1045" y2="101"/>
    <line x1="632" y1="128" x2="661" y2="128"/>
    <line x1="632" y1="667" x2="661" y2="667"/>
    <line x1="646.5" y1="128" x2="646.5" y2="667"/>
  </svg>
  <span class="dimension-text" style="left:357px;top:74px">60 mm.</span>
  <span class="dimension-text vertical" style="left:140px;top:399px">90 mm.</span>
  <span class="dimension-text" style="left:847px;top:74px">60 mm.</span>
  <span class="dimension-text vertical" style="left:630px;top:399px">90 mm.</span>

  <!-- Front label -->
  <section class="label label-front" style="left:196px">
    <div class="label-ornament" role="img" aria-label="Dark red traditional floral damask pattern"></div>
    <svg class="label-panel" viewBox="0 0 260 449" aria-hidden="true">
      <path class="panel-fill" d="M0 0H260V449q-9.29 -12 -18.57 0q-9.29 -12 -18.57 0q-9.29 -12 -18.57 0q-9.29 -12 -18.57 0q-9.29 -12 -18.57 0q-9.29 -12 -18.57 0q-9.29 -12 -18.57 0q-9.29 -12 -18.57 0q-9.29 -12 -18.57 0q-9.29 -12 -18.57 0q-9.29 -12 -18.57 0q-9.29 -12 -18.57 0q-9.29 -12 -18.57 0q-9.29 -12 -18.57 0Z"/>
      <line class="panel-rule" x1="8" y1="0" x2="8" y2="432"/>
      <line class="panel-rule" x1="252" y1="0" x2="252" y2="432"/>
    </svg>
    <h1 class="brand-name" style="left:50px;width:260px">KORVA</h1>
    <div class="tagline-band" style="left:78px"><p class="tagline">Artisan quality</p></div>
  </section>

  <!-- Back label -->
  <section class="label label-back" style="left:686px">
    <div class="label-ornament" role="img" aria-label="Dark red traditional floral damask pattern"></div>
    <svg class="label-panel" viewBox="0 0 260 449" aria-hidden="true">
      <path class="panel-fill" d="M0 0H260V449q-9.29 -12 -18.57 0q-9.29 -12 -18.57 0q-9.29 -12 -18.57 0q-9.29 -12 -18.57 0q-9.29 -12 -18.57 0q-9.29 -12 -18.57 0q-9.29 -12 -18.57 0q-9.29 -12 -18.57 0q-9.29 -12 -18.57 0q-9.29 -12 -18.57 0q-9.29 -12 -18.57 0q-9.29 -12 -18.57 0q-9.29 -12 -18.57 0q-9.29 -12 -18.57 0Z"/>
      <line class="panel-rule" x1="8" y1="0" x2="8" y2="432"/>
      <line class="panel-rule" x1="252" y1="0" x2="252" y2="432"/>
    </svg>
    <div class="tagline-band" style="left:78px"></div>
  </section>

</main>
</body>
</html>
```